Keystone Nest Checks Inspection Report Stationary

I require some new stationary for my home inspection reports in PDF. A first page then second page and beyond. We have plenty of marketing material on our website to get an idea about us and I have attached a copy of what it looks like now and our logo's in EPS. Just looking for something a little more attractive than our plain stationary. www.keystonenestchecks.com

Target Market(s)

New home owners

Industry/Entity Type

Home Inspection

Font styles to use
Sans Serif

Colors
ec1f27

Requirements
Must have
• Our Keystone Nest Checks Colors
Nice to have
• sorry no clue
Should not have
• It can't bee too large becasue we are basically pasting our report in it.

```html
<!DOCTYPE html>
<html lang="en">
<head>
<meta charset="utf-8">
<title>Keystone Nest Checks – Inspection Report Page</title>
<link rel="stylesheet" href="https://fonts.googleapis.com/css2?family=Open+Sans:wght@400;600;700&display=swap">
<style>
  :root{
    --brand-red:#ec1f27;
    --ink:#2b2b2b;
    --bar-grey:#cfcfcf;
    --page:#ffffff;
    --rule:#d9d9d9;
  }
  *{box-sizing:border-box;margin:0;padding:0}
  html,body{width:849px;height:1200px;overflow:hidden;background:var(--page)}
  body{font-family:"Open Sans",Arial,sans-serif;color:var(--ink);position:relative}
  .page{position:relative;width:849px;height:1200px}

  .masthead{position:absolute;left:28px;right:28px;top:14px;height:64px;display:flex;justify-content:space-between;align-items:flex-start}
  .brand{display:flex;align-items:center;gap:10px;margin-top:6px}
  .brand-square{width:44px;height:44px;background:var(--brand-red)}
  .brand-name{font-size:24px;font-weight:700;color:var(--brand-red);letter-spacing:.2px}
  .property-address{font-size:17px;font-weight:700;color:var(--ink);margin-top:14px}

  .section-bar{position:absolute;left:28px;right:28px;height:24px;background:var(--bar-grey);
    font-size:16px;font-weight:700;text-align:center;line-height:24px;color:var(--ink)}

  .observations{position:absolute;left:60px;right:60px;font-size:13px;line-height:17px;text-align:center}

  .photo-pair{position:absolute;left:34px;right:28px;display:flex;gap:12px}
  .photo{flex:1;height:100%}

  .columns{position:absolute;left:32px;right:32px;top:738px;display:flex;gap:22px;font-size:13px;line-height:17px}
  .columns p{flex:1}

  .page-footer{position:absolute;left:0;right:0;top:1150px;height:32px;background:var(--brand-red);
    color:#fff;font-weight:700;font-size:15px;text-align:center;line-height:32px}
</style>
</head>
<body>
<div class="page">
  <header class="masthead">
    <div class="brand">
      <span class="brand-square"></span>
      <span class="brand-name">Keystone Nest Checks</span>
    </div>
    <div class="property-address">418 Larkspur Crescent NE, Calgary, AB</div>
  </header>

  <h2 class="section-bar" style="top:86px">2. Joists Conditions</h2>
  <div class="observations" style="top:114px">
    Observations:<br>
    • 2x10 joists noted<br>
    • Appears Functional.<br>
    • Some areas are not visible for inspection due to wall/ceilings covered which prevents review of structural members.
  </div>
  <div class="photo-pair" style="top:192px;height:204px">
    <div class="photo" role="img" aria-label="Photo of exposed floor joists in basement" style="background:linear-gradient(160deg,#8a7a66,#c49a6a 45%,#6e6256)"></div>
    <div class="photo" role="img" aria-label="Photo of joists beside a heating duct" style="background:linear-gradient(200deg,#d8b07a,#a58866 50%,#c9bda8)"></div>
  </div>

  <h2 class="section-bar" style="top:410px">3. Post and Beams</h2>
  <div class="observations" style="top:438px">
    Observations:<br>
    • No deficiencies were observed at the visible portions of the structural components of the home. See Limitations.<br>
    • Posts and beams are partially finished, unable to fully inspect.<br>
    • Steel posts noted.<br>
    • Beam Material: Wood
  </div>
  <div class="photo-pair" style="top:548px;height:150px">
    <div class="photo" role="img" aria-label="Photo of steel post in unfinished basement" style="background:linear-gradient(160deg,#b9b9b4,#e6e4de 50%,#9c9a94)"></div>
    <div class="photo" role="img" aria-label="Photo of wooden beam resting on a post" style="background:linear-gradient(200deg,#d9d6cf,#b49b7a 45%,#8f8b84)"></div>
  </div>

  <h2 class="section-bar" style="top:707px">4. Slab Flooring</h2>
  <div class="columns">
    <p>Observations:<br>
    • Cracks in a concrete slab are not directly related to the structural integrity of the home. The potential for water seepage through the cracks exists, if the area is in a high water table and/or if negative drainage exists. All surface water must be directed away from the foundation to reduce possible moisture intrusion into basement. Our moisture readings and observations are not conclusive, and we cannot provide any guarantee that moisture will not enter the basement in the future. No moisture readings were detected on the concrete slab or floor coverings, this condition may vary seasonally.</p>
    <p>• Entire concrete slab not visible due to floor coverings.<br>
    • All concrete floor slabs experience some degree of cracking due to shrinkage in the drying process. In most instances floor coverings prevent recognition of cracks or settlement in all but the most severe cases. Where carpeting and other floor coverings are installed, the materials and condition of the flooring underneath cannot be determined.<br>
    • Visible areas appear satisfactory.<br>
    • Common cracks noted. Recommend consultation with qualified contractor should condition worsen or water intrusion occur.</p>
  </div>

  <footer class="page-footer">Page 11 of 50</footer>
</div>
</body>
</html>
```